CD Cover Design

Listing down some requirements:

1.Pastel color scheme (ie: baby pink, light blue, light green, pale yellow, white, silver, baby pastel purple etc.) i.e: a very sweet, dreamy and girly feel

2. Name of artist: Clara Vendt
Name of Album: Lanterns: The 1st Full Length Album
(To be added into the design of the album cover, preferably name of artist in the centre middle and name of album to be below)

Note: I wish for a feminine and classy cd cover instead of a cartoony and children-like design thankyou! Hope to not have misunderstandings because I uploaded cute graphic pictures as references! Indeed I would like the cd cover to be designed by those graphic cartoons but with a feminine and classy elegant touch instead of that like a children's album. Thank you!

3. Usage of pastel cartoon designs (like the uploaded references)

Industry/Entity Type

Baby

Font styles to use
Script

Colors
d3a5cc
b768aa
eda3c7
ecdaeb
f6f0f7
cde9f5
e9f1ce
fdf9ce

Requirements
Should not have
• Over crowding of cartoons
Ie: Don't fill the whole design with the cartoons, space them out so that it don't look so messy

```html
<!DOCTYPE html>
<html lang="en">
<head>
<meta charset="utf-8">
<title>Clara Vendt – Lanterns: The 1st Full Length Album</title>
<link rel="stylesheet" href="https://fonts.googleapis.com/css2?family=Pinyon+Script&family=Arimo&display=swap">
<style>
  :root {
    --stage: #d9d9d9;
    --disc: #b768aa;
    --disc-edge: #a95d9c;
    --hub: #6f6f6f;
    --hub-ring: #7d7d7d;
    --hole: #8f8f8f;
    --ink-light: #ffffff;
    --doodle-cream: #fdf9ce;
    --doodle-lilac: #d3a5cc;
    --doodle-pink: #eda3c7;
    --doodle-mist: #ecdaeb;
  }
  html, body {
    margin: 0;
    padding: 0;
    width: 1200px;
    height: 1198px;
    overflow: hidden;
    background: var(--stage);
  }
  .cd-label {
    display: block;
    width: 1200px;
    height: 1198px;
  }
  .disc { fill: var(--disc); stroke: var(--disc-edge); stroke-width: 4; }
  .hub { fill: var(--hub); }
  .hub-ring { fill: var(--hub-ring); }
  .hub-hole { fill: var(--hole); stroke: #5c5c5c; stroke-width: 3; }
  .artist-name {
    font-family: "Pinyon Script", cursive;
    font-size: 52px;
    fill: var(--ink-light);
  }
  .album-title {
    font-family: "Pinyon Script", cursive;
    font-size: 132px;
    fill: var(--ink-light);
  }
  .album-subtitle {
    font-family: "Arimo", Arial, sans-serif;
    font-size: 30px;
    fill: var(--ink-light);
  }
  .star {
    fill: var(--doodle-mist);
    fill-opacity: 0.35;
    stroke: var(--doodle-mist);
    stroke-opacity: 0.8;
    stroke-width: 3;
    stroke-linejoin: round;
  }
  .heart {
    fill: none;
    stroke: var(--doodle-pink);
    stroke-opacity: 0.8;
    stroke-width: 9;
    stroke-linejoin: round;
  }
</style>
</head>
<body>
<svg class="cd-label" viewBox="0 0 1200 1198" xmlns="http://www.w3.org/2000/svg">
  <defs>
    <radialGradient id="glow-cream">
      <stop offset="0" stop-color="#fdf9ce" stop-opacity="0.75"/>
      <stop offset="0.55" stop-color="#fdf9ce" stop-opacity="0.35"/>
      <stop offset="1" stop-color="#fdf9ce" stop-opacity="0"/>
    </radialGradient>
    <radialGradient id="glow-mist">
      <stop offset="0" stop-color="#ecdaeb" stop-opacity="0.6"/>
      <stop offset="1" stop-color="#ecdaeb" stop-opacity="0"/>
    </radialGradient>
    <radialGradient id="glow-lilac">
      <stop offset="0" stop-color="#d3a5cc" stop-opacity="0.55"/>
      <stop offset="1" stop-color="#d3a5cc" stop-opacity="0"/>
    </radialGradient>
    <polygon id="star-shape" points="0,-38 10,-12 37,-12 15,5 23,31 0,15 -23,31 -15,5 -37,-12 -10,-12"/>
  </defs>

  <circle class="disc" cx="600" cy="599" r="586"/>

  <circle cx="706" cy="190" r="95" fill="url(#glow-cream)" role="img" aria-label="Hand-drawn pale yellow sun doodle"/>
  <ellipse cx="876" cy="371" rx="90" ry="62" fill="url(#glow-mist)" role="img" aria-label="Hand-drawn masquerade mask doodle"/>
  <circle cx="886" cy="717" r="70" fill="url(#glow-cream)" role="img" aria-label="Pale yellow full moon doodle"/>
  <ellipse cx="215" cy="830" rx="100" ry="185" fill="url(#glow-lilac)" role="img" aria-label="Curling vine ornament with small hearts"/>

  <use class="star" href="#star-shape" x="485" y="114"/>
  <use class="star" href="#star-shape" x="265" y="388"/>
  <use class="star" href="#star-shape" x="1069" y="458"/>
  <use class="star" href="#star-shape" x="960" y="589"/>
  <use class="star" href="#star-shape" x="762" y="1019"/>

  <path class="heart" d="M129,592 C95,565 68,545 68,518 C68,497 84,484 102,484 C115,484 124,492 129,502 C134,492 143,484 156,484 C174,484 190,497 190,518 C190,545 163,565 129,592 Z"/>

  <circle class="hub" cx="600" cy="599" r="178"/>
  <circle class="hub-ring" cx="600" cy="599" r="122"/>
  <circle class="hub-hole" cx="600" cy="599" r="62"/>

  <text class="artist-name" x="606" y="338" text-anchor="middle">Clara Vendt</text>
  <text class="album-title" x="340" y="898">Lanterns:</text>
  <text class="album-subtitle" x="448" y="948">The 1st Full Length</text>
</svg>
</body>
</html>
```